Business Card Design

Buy and sell properties
Buy and rehab properties
Buy properties for cash
That is what I do but do need a logo
looking for some type of logo or design on it
Just started business
Back of card should say something like BUY HOUSES CASH
Overview: it is a new company. Basically I buy properties wholesale and fix them up and sell them or sell them to other fix and flippers
Background: company is new so not any background
Market: is basically anyone selling a house or buying a house. Someone that needs to sell house fast. Basically I am a cash home buyer!!!

Updates
Email on card should be:   harborlanerealtyinc@mailbox.test

Industry/Entity Type
House
Contact Information for Business Card
Harbor Lane Realty Inc
PO Box 718269
Cedar Marsh FL 32987

Dale Morrick
dmorrick@mailbox.test
555-271-6094

```html
<!DOCTYPE html>
<html lang="en">
<head>
<meta charset="utf-8">
<title>Harbor Lane Realty Inc – Business Card</title>
<link rel="stylesheet" href="https://fonts.googleapis.com/css2?family=Ubuntu:wght@400;500;700&display=swap">
<style>
  :root {
    --page: #d9d9d9;
    --card: #fbfbfa;
    --blue: #1b6fb0;
    --blue-light: #2386c4;
    --blue-text: #1565a8;
    --white-text: #e9f3fa;
    --shadow: rgba(0, 0, 0, 0.22);
  }
  * { box-sizing: border-box; margin: 0; padding: 0; }
  html, body { width: 1200px; height: 1000px; overflow: hidden; }
  body {
    background: var(--page);
    font-family: "Ubuntu", sans-serif;
    position: relative;
  }
  .card {
    position: absolute;
    width: 640px;
    height: 366px;
    background: var(--card);
    box-shadow: 0 6px 18px var(--shadow);
    overflow: hidden;
  }

  /* Front */
  .card-front { left: 500px; top: 70px; }
  .card-front .brand {
    position: absolute;
    left: 0; right: 0; top: 120px;
    display: flex; justify-content: center; align-items: center; gap: 16px;
  }
  .brand-mark {
    width: 34px; height: 34px;
    background: var(--blue);
    flex: none;
  }
  .brand-name {
    font-weight: 500;
    color: var(--blue-text);
    font-size: 34px;
    white-space: nowrap;
  }
  .card-front .front-email {
    position: absolute;
    left: 0; right: 0; bottom: 68px;
    text-align: center;
    color: var(--blue-text);
    font-weight: 500;
    font-size: 17px;
    letter-spacing: 0.22em;
  }

  /* Back */
  .card-back { left: 60px; top: 520px; }
  .panel-top {
    position: absolute; left: 0; top: 0;
    width: 60%; height: 76px;
    background: linear-gradient(90deg, var(--blue), var(--blue-light));
  }
  .panel-bottom {
    position: absolute; left: 0; bottom: 0;
    width: 54%; height: 150px;
    background: linear-gradient(90deg, var(--blue), var(--blue-light));
  }
  .rule {
    position: absolute; left: 0;
    height: 9px;
    background: var(--blue);
  }
  .rule-one { top: 132px; width: 56%; }
  .rule-two { top: 180px; width: 55%; }
  .contact-name {
    position: absolute; left: 0; width: 58%; top: 86px;
    text-align: center;
    color: var(--blue-text);
    font-weight: 700;
    font-size: 25px;
  }
  .contact-line {
    position: absolute; left: 0; width: 56%;
    text-align: center;
    color: var(--blue-text);
    font-size: 19px;
  }
  .contact-phone { top: 148px; }
  .contact-email { top: 193px; }
  .address {
    position: absolute; left: 28px; bottom: 24px;
    color: var(--white-text);
    font-size: 17px;
    line-height: 1.4;
  }
  .address .company { font-size: 22px; margin-bottom: 4px; }
  .card-back .brand {
    position: absolute;
    left: 58%; right: 0; top: 140px;
    display: flex; justify-content: center; align-items: center; gap: 10px;
  }
  .card-back .brand-mark { width: 20px; height: 20px; }
  .card-back .brand-name { font-size: 20px; }
  .tagline {
    position: absolute;
    left: 56%; right: 0; bottom: 32px;
    text-align: center;
    color: var(--blue-text);
    font-weight: 500;
    font-size: 20px;
    letter-spacing: 0.22em;
  }
</style>
</head>
<body>
  <section class="card card-front" aria-label="Card front">
    <div class="brand">
      <span class="brand-mark"></span>
      <span class="brand-name">Harbor Lane Realty Inc</span>
    </div>
    <p class="front-email">harborlanerealtyinc@mailbox.test</p>
  </section>

  <section class="card card-back" aria-label="Card back">
    <div class="panel-top"></div>
    <div class="rule rule-one"></div>
    <div class="rule rule-two"></div>
    <div class="panel-bottom"></div>

    <p class="contact-name">Dale Morrick</p>
    <p class="contact-line contact-phone">Phone : 555-271-6094</p>
    <p class="contact-line contact-email">Email : dmorrick@mailbox.test</p>

    <address class="address" style="font-style: normal;">
      <div class="company">Harbor Lane Realty Inc</div>
      <div>PO Box 718269</div>
      <div>Cedar Marsh FL 32987</div>
    </address>

    <div class="brand">
      <span class="brand-mark"></span>
      <span class="brand-name">Harbor Lane Realty Inc</span>
    </div>
    <p class="tagline">BUY HOUSES CASH</p>
  </section>
</body>
</html>
```